The Bridgewell Counseling Group - Practice Flyer

We need a flyer that generally advertises our services. I've uploaded one old flyer as well as examples of others. I like the style of the materials made by this practice: https://www.facebook.com/MarlowTherapyStudioNorth

```html
<!DOCTYPE html>
<html lang="en">
<head>
<meta charset="utf-8">
<title>The Bridgewell Counseling Group – Practice Flyer</title>
<link rel="stylesheet" href="https://fonts.googleapis.com/css2?family=Ubuntu:wght@400;500;700&family=PT+Sans:wght@400;700&display=swap">
<style>
  :root {
    --forest: #2b4128;
    --olive: #8c9660;
    --olive-light: #a3ab78;
    --white: #ffffff;
    --ink: #2f3a2c;
    --social-blue: #3b5998;
    --social-sky: #1da1f2;
    --social-red: #e52d27;
  }
  * { box-sizing: border-box; margin: 0; padding: 0; }
  html, body { width: 1014px; height: 1200px; overflow: hidden; background: #4a4a4c; }
  .flyer {
    position: relative; width: 1014px; height: 1200px; overflow: hidden;
    background: var(--white); font-family: "PT Sans", sans-serif; color: var(--ink);
  }
  .scene-photo {
    position: absolute; left: 0; top: 582px; width: 1014px; height: 618px;
    background: linear-gradient(100deg, #6f6c5a 0%, #8e7d5c 35%, #c29a5e 65%, #d8b277 85%, #b8955d 100%);
  }
  .brand { position: absolute; left: 0; top: 66px; width: 1014px; text-align: center; }
  .brand-name {
    font-family: "Ubuntu", sans-serif; font-weight: 500; font-size: 54px; line-height: 62px;
    color: var(--forest); letter-spacing: 1px;
  }
  .brand-rule { width: 720px; height: 4px; background: var(--olive); margin: 14px auto 26px; }
  .brand-sub {
    font-family: "Ubuntu", sans-serif; font-size: 20px; letter-spacing: 2px;
    color: var(--forest); text-transform: uppercase;
  }
  .intro {
    position: absolute; left: 538px; top: 254px; width: 440px;
    font-size: 17px; line-height: 21px; text-align: justify;
  }
  .diamond { position: absolute; width: 158px; height: 158px; transform: rotate(45deg); }
  .d1 { left: 129px; top: 284px; background: linear-gradient(135deg, #e9d5a6, #c9a875 60%, #8f6f4a); }
  .d2 { left: 287px; top: 428px; background: linear-gradient(135deg, #eed9b0, #8fc1bb 55%, #6ea7a2); }
  .d3 { left: 132px; top: 570px; background: linear-gradient(135deg, #dfe6d8, #7ea3c4 55%, #6d8aa6); }
  .frames { position: absolute; left: 0; top: 0; }
  .disorders {
    position: absolute; left: 525px; top: 398px; width: 489px; height: 238px;
    background: var(--forest); color: var(--white); padding: 13px 20px 0 26px;
    border-left: 6px solid #1f2f1d;
  }
  .disorders p { font-size: 16px; line-height: 20px; }
  .disorders .list {
    margin-top: 18px; font-family: "Ubuntu", sans-serif; font-weight: 500;
    font-size: 16px; line-height: 20px; text-align: justify;
  }
  .dot { color: var(--olive-light); }
  .cbt-note {
    position: absolute; left: 525px; top: 636px; width: 489px; height: 120px;
    background: var(--olive); color: var(--white); padding: 14px 30px 0 28px;
    font-size: 17px; line-height: 20px; text-align: justify;
  }
  .contact { position: absolute; left: 530px; width: 480px; text-align: center; }
  .tel-label { top: 786px; color: var(--olive); font-family: "Ubuntu", sans-serif; font-size: 16px; }
  .tel { top: 804px; font-family: "Ubuntu", sans-serif; font-weight: 700; font-size: 50px; color: var(--forest); }
  .director { top: 872px; line-height: 1; color: var(--forest); font-family: "Ubuntu", sans-serif; }
  .director .name { font-size: 17px; }
  .director .role { font-size: 22px; font-weight: 700; margin-top: 6px; }
  .director .cred { font-size: 14px; margin-top: 4px; }
  .license {
    position: absolute; top: 966px; width: 212px; height: 70px;
    border: 2px solid var(--white); border-radius: 10px; text-align: center; padding-top: 6px;
  }
  .license.nj { left: 550px; }
  .license.pa { left: 771px; }
  .license .label { color: var(--white); font-size: 15px; font-family: "Ubuntu", sans-serif; }
  .license .num { color: var(--forest); font-family: "Ubuntu", sans-serif; font-weight: 700; font-size: 23px; margin-top: 2px; }
  .web { top: 1060px; left: 520px; width: 494px; color: var(--white); font-family: "Ubuntu", sans-serif; font-weight: 700; font-size: 21px; }
  .find { top: 1104px; left: 520px; width: 490px; color: var(--white); font-family: "Ubuntu", sans-serif; font-weight: 500; font-size: 15px; }
  .social { position: absolute; top: 1134px; left: 652px; display: flex; gap: 22px; }
  .social span { width: 54px; height: 54px; border-radius: 50%; display: block; }
  .social .s1 { background: var(--social-blue); }
  .social .s2 { background: var(--social-sky); }
  .social .s3 { background: var(--social-red); }
  .mark {
    position: absolute; left: 975px; top: 1151px; width: 39px; height: 49px;
    background: var(--forest); color: var(--white); font-family: "Ubuntu", sans-serif;
    font-weight: 700; font-size: 13px; display: flex; align-items: flex-end; justify-content: center; padding-bottom: 6px;
  }
  .treat-title {
    position: absolute; left: 12px; top: 818px; color: var(--white);
    font-family: "Ubuntu", sans-serif; font-weight: 700; font-size: 35px; line-height: 40px;
  }
  .treat-panel {
    position: absolute; left: 0; top: 924px; width: 503px; height: 276px;
    background: rgba(255,255,255,0.72); border-top-right-radius: 40px; padding: 30px 36px 0 14px;
  }
  .treat-panel ul { list-style: none; }
  .treat-panel li {
    position: relative; padding-left: 37px; font-family: "Ubuntu", sans-serif; font-weight: 500;
    font-size: 19px; line-height: 20px; color: var(--forest); margin-bottom: 6px;
  }
  .treat-panel li svg { position: absolute; left: 0; top: 0; }
</style>
</head>
<body>
<div class="flyer">
  <div class="scene-photo" role="img" aria-label="Family walking along a sunlit country path at golden hour"></div>

  <header class="brand">
    <div class="brand-name">The Bridgewell Counseling Group</div>
    <div class="brand-rule"></div>
    <div class="brand-sub">of Greater Philadelphia LLC</div>
  </header>

  <p class="intro">The Bridgewell Counseling Group of Greater Philadelphia, (BCG) provides expert clinical care for anxiety disorders, obsessive compulsive and related disorders, and neurodevelopmental disorders in children, adolescents, and adults.</p>

  <div class="diamond d1" role="img" aria-label="Smiling older couple embracing in a kitchen"></div>
  <div class="diamond d2" role="img" aria-label="Cheerful young woman in a teal sweater dancing"></div>
  <div class="diamond d3" role="img" aria-label="Person sitting cross-legged on the floor, relaxed"></div>

  <svg class="frames" width="1014" height="1200" aria-hidden="true">
    <polyline points="254,284 291,250 484,427 449,459" fill="none" stroke="var(--forest)" stroke-width="3"/>
    <polyline points="453,557 492,590 299,768 260,732" fill="none" stroke="var(--forest)" stroke-width="3"/>
  </svg>

  <section class="disorders">
    <p>BCG proudly provides the Greater Philadelphia community with state-of-the-art assessment and evidence-based therapy for disorders including:</p>
    <p class="list">Obsessive Compulsive Disorder <span class="dot">●</span> Trichotillomania Excoriation Disorder <span class="dot">●</span> Generalized Anxiety Disorder Panic Disorder <span class="dot">●</span> Specific Phobias <span class="dot">●</span> Hoarding Disorder Body Dysmorphic Disorder <span class="dot">●</span> Tic Disorders <span class="dot">●</span> ADHD Learning Disorders <span class="dot">●</span> Insomnia <span class="dot">●</span> Social Anxiety Disorder</p>
  </section>

  <p class="cbt-note">BCG clinicians are highly trained in cognitive behavioral therapy (CBT), which includes scientifically informed techniques that are tailored to each client's unique needs.</p>

  <div class="contact tel-label">TELEPHONE</div>
  <div class="contact tel">(856) 555-0142</div>
  <div class="contact director">
    <div class="name">Helen R. Ashford, PsyD</div>
    <div class="role">Executive Director</div>
    <div class="cred">Licensed Clinical Psychologist</div>
  </div>

  <div class="license nj"><div class="label">New Jersey License No.</div><div class="num">35S10098217</div></div>
  <div class="license pa"><div class="label">Pennsylvania Lic. No.</div><div class="num">PS0162483</div></div>

  <div class="contact web">www.BridgewellCounselingGroup.com</div>
  <div class="contact find">Find Us on</div>
  <div class="social" aria-label="Social media links">
    <span class="s1"></span>
    <span class="s2"></span>
    <span class="s3"></span>
  </div>

  <h2 class="treat-title">TREATMENTS WE PROVIDE</h2>
  <section class="treat-panel">
    <ul>
      <li><svg width="22" height="20" viewBox="0 0 22 20"><circle cx="10" cy="11" r="8" fill="none" stroke="#9aa07a" stroke-width="1.5"/><path d="M5 10l4 5 10-12" fill="none" stroke="var(--olive)" stroke-width="3"/></svg>Cognitive Behavioral Therapy (CBT)</li>
      <li><svg width="22" height="20" viewBox="0 0 22 20"><circle cx="10" cy="11" r="8" fill="none" stroke="#9aa07a" stroke-width="1.5"/><path d="M5 10l4 5 10-12" fill="none" stroke="var(--olive)" stroke-width="3"/></svg>Exposure and Response Prevention (E/RP)</li>
      <li><svg width="22" height="20" viewBox="0 0 22 20"><circle cx="10" cy="11" r="8" fill="none" stroke="#9aa07a" stroke-width="1.5"/><path d="M5 10l4 5 10-12" fill="none" stroke="var(--olive)" stroke-width="3"/></svg>Comprehensive Behavioral (ComB)/Habit Reversal Training (HRT)</li>
      <li><svg width="22" height="20" viewBox="0 0 22 20"><circle cx="10" cy="11" r="8" fill="none" stroke="#9aa07a" stroke-width="1.5"/><path d="M5 10l4 5 10-12" fill="none" stroke="var(--olive)" stroke-width="3"/></svg>Cognitive Behavioral Intervention for Tics (CBIT)</li>
      <li><svg width="22" height="20" viewBox="0 0 22 20"><circle cx="10" cy="11" r="8" fill="none" stroke="#9aa07a" stroke-width="1.5"/><path d="M5 10l4 5 10-12" fill="none" stroke="var(--olive)" stroke-width="3"/></svg>Acceptance and Commitment Therapy (ACT)</li>
      <li><svg width="22" height="20" viewBox="0 0 22 20"><circle cx="10" cy="11" r="8" fill="none" stroke="#9aa07a" stroke-width="1.5"/><path d="M5 10l4 5 10-12" fill="none" stroke="var(--olive)" stroke-width="3"/></svg>Organizational Skills Training (OST)</li>
      <li><svg width="22" height="20" viewBox="0 0 22 20"><circle cx="10" cy="11" r="8" fill="none" stroke="#9aa07a" stroke-width="1.5"/><path d="M5 10l4 5 10-12" fill="none" stroke="var(--olive)" stroke-width="3"/></svg>CBT for Insomnia (CBT-I)</li>
    </ul>
  </section>

  <div class="mark">BCG</div>
</div>
</body>
</html>
```